Broschüre für Gebäudereinigungsservice
Zielgruppe
Wir sind ein Gebäudeservice Unterehmen. Wir sind spezialisiert auf: Reinigungen aller Art, Grünflächenpflege aller Art, Winterdienst und Handwerkerservice aller Art. Usere Zielgruppe: Hausverwaltungen, Genossenschaften und Privatpersonen.
Aufgabenstellung
Die Broschüre soll an diese Kunden per Mail als auch ausgedruckt versendet werden.
Kunden sollen mit dieser Broschüre davon überzeugt werden uns als Gebäudeservice-Unternehmen zu beauftragen.
Unser Firmenslogan lautet 'QUALITÄT DURCH LEISTUNG.'
Die Bilder im Anhang können übernommen werden. Müssen aber nicht, bin für besserer Vorschläge gerne zu haben.
Alle Formate sind erlaubt
Bei Fragen bitte kontaktieren.
Danke!

```html
<!DOCTYPE html>
<html lang="de">
<head>
<meta charset="utf-8">
<title>Velora Gebäudeservice – Broschüre</title>
<link rel="stylesheet" href="https://fonts.googleapis.com/css2?family=Barlow:wght@400;600;700&family=Barlow+Semi+Condensed:wght@700&display=swap">
<style>
  :root{
    --orange:#e8540f;
    --red:#d8361a;
    --text:#2b2b2b;
    --paper:#ffffff;
    --bg:#ffffff;
  }
  *{margin:0;padding:0;box-sizing:border-box}
  html,body{width:801px;height:1200px;overflow:hidden;background:var(--bg);font-family:"Barlow",sans-serif;color:var(--text)}
  .page{position:absolute;left:159px;width:479px;height:478px;background:var(--paper);overflow:hidden;box-shadow:3px 4px 6px rgba(0,0,0,.35)}
  .page--cover{top:87px}
  .page--services{top:647px}
  .page__art{position:absolute;inset:0}
  .headline{position:absolute;left:203px;top:47px;color:#fff;font-family:"Barlow Semi Condensed",sans-serif;font-weight:700;font-size:25px;line-height:24px;letter-spacing:1.5px}
  .intro{position:absolute;left:23px;top:234px;width:147px;font-size:6.2px;line-height:11.3px;text-align:justify;hyphens:auto;-webkit-hyphens:auto}
  .intro__motto{color:var(--orange);font-weight:600;font-size:7.2px;letter-spacing:.4px;margin:9px 0 11px;text-align:left}
  .brand{position:absolute;left:212px;top:350px;color:var(--orange);font-weight:700;font-size:36px;line-height:34px;letter-spacing:1px}
  .brand span{display:block;color:#3a3a3a;font-size:12.4px;line-height:16px;letter-spacing:2.6px}
  .contact{position:absolute;top:427px;font-size:7.2px;line-height:11.5px;letter-spacing:.6px}
  .contact--address{left:212px}
  .contact--reach{left:334px}
  .contact--reach b{display:inline-block;width:27px;font-weight:600}
  .service{position:absolute;width:94px}
  .service h2{color:var(--red);font-size:7.6px;font-weight:700;letter-spacing:.3px;margin-bottom:3px}
  .service ul{list-style:none}
  .service li{font-size:4.6px;line-height:9px;padding-left:5px;position:relative}
  .service li::before{content:"";position:absolute;left:0;top:3.5px;width:2px;height:2px;background:var(--red);border-radius:50%}
</style>
</head>
<body>

<svg width="0" height="0" style="position:absolute">
  <defs>
    <linearGradient id="scene" x1="0" y1="0" x2="1" y2="0.25">
      <stop offset="0" stop-color="#e4e8ec"/>
      <stop offset=".22" stop-color="#b9c3cc"/>
      <stop offset=".42" stop-color="#8fb9de"/>
      <stop offset=".58" stop-color="#3d8fd8"/>
      <stop offset=".78" stop-color="#4f94c9"/>
      <stop offset=".9" stop-color="#4f8a34"/>
      <stop offset="1" stop-color="#2f6a22"/>
    </linearGradient>
    <linearGradient id="skyfade" x1="0" y1="0" x2="0" y2="1">
      <stop offset="0" stop-color="#1f7fd0" stop-opacity=".55"/>
      <stop offset=".55" stop-color="#1f7fd0" stop-opacity="0"/>
    </linearGradient>
    <linearGradient id="clean" x1="0" y1="0" x2="1" y2="1">
      <stop offset="0" stop-color="#f4f5f6"/><stop offset=".6" stop-color="#d8cbb8"/><stop offset="1" stop-color="#8a7a66"/>
    </linearGradient>
    <linearGradient id="craft" x1="0" y1="0" x2="1" y2="1">
      <stop offset="0" stop-color="#c9d0d4"/><stop offset=".5" stop-color="#d9b49a"/><stop offset="1" stop-color="#4f8f6a"/>
    </linearGradient>
    <linearGradient id="lawn" x1="0" y1="0" x2="0" y2="1">
      <stop offset="0" stop-color="#eef2f4"/><stop offset=".35" stop-color="#7fb84a"/><stop offset="1" stop-color="#3d7d22"/>
    </linearGradient>
    <linearGradient id="winter" x1="0" y1="0" x2="1" y2="1">
      <stop offset="0" stop-color="#dfe6ec"/><stop offset=".55" stop-color="#b6c2cc"/><stop offset="1" stop-color="#4d5a64"/>
    </linearGradient>
    <linearGradient id="junk" x1="0" y1="0" x2="1" y2="1">
      <stop offset="0" stop-color="#d9e3ea"/><stop offset=".5" stop-color="#8fb0c6"/><stop offset="1" stop-color="#8a7560"/>
    </linearGradient>
  </defs>
</svg>

<section class="page page--cover">
  <svg class="page__art" viewBox="0 0 479 478" width="479" height="478">
    <g role="img" aria-label="Foto: modernes Wohngebäude mit Balkonen vor blauem Himmel und Bäumen">
      <rect width="479" height="478" fill="url(#scene)"/>
      <rect width="479" height="478" fill="url(#skyfade)"/>
    </g>
    <path d="M0,180 Q150,194 257,234 Q390,300 479,392 L479,478 L0,478Z" fill="var(--paper)"/>
    <path d="M0,176 Q150,190 240,222" fill="none" stroke="var(--orange)" stroke-width="6"/>
    <path d="M275,240 Q395,296 479,388" fill="none" stroke="var(--red)" stroke-width="4"/>
    <circle cx="257" cy="248" r="42" fill="var(--paper)"/>
    <circle cx="257" cy="248" r="38" fill="var(--red)"/>
    <circle cx="257" cy="248" r="30" fill="none" stroke="var(--paper)" stroke-width="1.5"/>
  </svg>
  <h1 class="headline">QUALITÄT DURCH<br>LEISTUNG</h1>
  <div class="intro">
    <p>Wir sind ein seit 2012 bestehendes Familienunternehmen welches nach folgendem Motto lebt:</p>
    <p class="intro__motto">"QUALITÄT DURCH LEISTUNG"</p>
    <p>Dieses Motto hat für uns die höchste Priorität, denn nur wenn sich alle Bewohner wirklich wohl fühlen, haben wir unser Ziel erreicht und unsere Idee verwirklicht. Diese kann nur mit kompetenten Mitarbeitern sowie durch regelmäßige Kontrollen der erbrachten Leistungen sichergestellt werden. Wir sind für unsere Kunden mit unserem Team bekannte Personen, und wir stellen uns immer wieder dem Gespräch mit unseren Kunden. Entscheidungsfreudige Mitarbeiter, die genau erkennen welche Bitten sofort erledigt werden können, oder welche dringend mit uns besprochen werden müssen, helfen die Qualität unserer Leistungen zu gewährleisten.</p>
  </div>
  <div class="brand">VELORA<span>GEBÄUDESERVICE</span></div>
  <p class="contact contact--address">Velora Gebäudeservice GmbH<br>Lindengasse 12/4<br>1220 Wien</p>
  <p class="contact contact--reach"><b>Tel:</b>01/555 20 48<br><b>Mail:</b>office@velora-service.at<br><b>Web:</b>www.velora-service.at</p>
</section>

<section class="page page--services">
  <svg class="page__art" viewBox="0 0 479 478" width="479" height="478">
    <g role="img" aria-label="Foto: modernes Wohngebäude mit Balkonen vor blauem Himmel und Bäumen">
      <rect width="479" height="478" fill="url(#scene)"/>
      <rect width="479" height="478" fill="url(#skyfade)"/>
    </g>
    <path d="M0,182 Q250,205 479,392 L479,478 L0,478Z" fill="var(--paper)"/>
    <path d="M0,178 Q250,201 479,388" fill="none" stroke="var(--orange)" stroke-width="6"/>
    <g stroke="var(--paper)" stroke-width="3">
      <circle cx="52" cy="185" r="38" fill="url(#clean)" role="img" aria-label="Foto: Reinigungskraft mit Wischmopp und Putzwagen"/>
      <circle cx="146" cy="208" r="38" fill="url(#craft)" role="img" aria-label="Foto: Handwerker mit Bohrmaschine"/>
      <circle cx="240" cy="240" r="38" fill="url(#lawn)" role="img" aria-label="Foto: Rasenmäher auf grüner Wiese"/>
      <circle cx="334" cy="279" r="38" fill="url(#winter)" role="img" aria-label="Foto: Winterdienst beim Schneeräumen"/>
      <circle cx="426" cy="326" r="38" fill="url(#junk)" role="img" aria-label="Foto: Sperrmüll und ausgeräumte Gegenstände"/>
    </g>
  </svg>

  <div class="service" style="left:8px;top:237px">
    <h2>Hausreinigung:</h2>
    <ul><li>wöchentliche Stiegenhausreinigung</li><li>Fensterreinigung</li><li>Büroreinigung</li><li>Wohnungsreinigung</li><li>Reinigung Außenflächen</li><li>Garagenassreinigung</li><li>Fassadenreinigung</li><li>Hochdruckreinigung</li><li>Graffitientfernung</li><li>diverse weitere Reinigungsarbeiten</li></ul>
  </div>
  <div class="service" style="left:101px;top:260px">
    <h2>Handwerker-Service:</h2>
    <ul><li>Reparatur Türen und Fenster</li><li>Kleinflächen verputzen und ausmalen</li><li>Reparatur und Montage Geländer und Handläufe</li><li>Montage Taubennetz und Taubenspitzen</li><li>Reparatur und Montage Gullys</li><li>Reparatur und Montage Türschließer</li><li>Instandsetzung Kaminmauerwerk und Kaminköpfe</li><li>Reparatur Holz-, Keramik- und Terazzoböden</li><li>Montage Kantenschutzprofile</li><li>Befestigung Boden- und Sockelfliesen</li><li>Reparatur gebrochene Betonstufen</li><li>diverse weitere Reparaturarbeiten</li></ul>
  </div>
  <div class="service" style="left:203px;top:291px">
    <h2>Grünflächenpflege:</h2>
    <ul><li>Rasenschnitt</li><li>Rasenbewässerung</li><li>Sträucherrückschnitt</li><li>Baumkronenrückschnitt</li><li>Baumrodung</li><li>Baumkronenabwurf</li><li>Wurzelstockfräsung</li><li>Efeubeseitigung</li><li>Fertigrasenverlegung</li><li>diverse weitere Grünflächen­pflegearbeiten</li></ul>
  </div>
  <div class="service" style="left:293px;top:329px">
    <h2>Winterdienst:</h2>
    <ul><li>Bereitschaftsdienst vom 01.11. bis 15.04.</li><li>Schneeräumung</li><li>Tauwetterkontrolle</li><li>Splitt- und Salzstreuung</li><li>Splittkehrung bei Trockenperioden</li><li>händische als auch maschinelle Räumung</li></ul>
  </div>
  <div class="service" style="left:382px;top:377px">
    <h2>Entrümpelung:</h2>
    <ul><li>Fachgerechte Abfallentsorgung</li><li>Sperrmüllentsorgung</li><li>Firmen- und Büroräumungen</li><li>Wohnungsräumungen</li><li>Verlassenschaftsräumungen</li><li>Dachboden- und Kellerräumungen</li><li>diverse weitere Räumungs- und Entrümpelungsarbeiten</li></ul>
  </div>
</section>

</body>
</html>
```